My project benefits Military, First Responders, Police, Fire, and Educators.

Contact Information for Business Card

2 Sided appointment card. Visual side will have my head shot with "Kestrel Works" in a bold graffic/text. I am picturing maybe the headshot applied to a filter that has a matrix effect where the picture is made up of data/numbers flowing vertically through the photo. I am of course open to other concepts as well. Side two will have contact info presented in an attractive visual complimenting the front.

```html
<!DOCTYPE html>
<html lang="en">
<head>
<meta charset="utf-8">
<title>Kestrel Works – Appointment Card</title>
<link href="https://fonts.googleapis.com/css2?family=Bebas+Neue&family=Cinzel:wght@400;500&family=Open+Sans:wght@400&display=swap" rel="stylesheet">
<style>
  :root {
    --backdrop: #e9e7e3;
    --card-black: #050505;
    --matrix-deep: #071a0c;
    --matrix-mid: #1a4a24;
    --photo-light: #5e7a60;
    --accent-green: #4a9a4c;
    --text-white: #f4f4f4;
    --divider: #7a7a7a;
  }
  * { margin: 0; padding: 0; box-sizing: border-box; }
  html, body { width: 1200px; height: 1000px; overflow: hidden; }
  body { background: var(--backdrop); position: relative; }

  .card {
    position: absolute;
    left: 267px;
    width: 665px;
    height: 397px;
    overflow: hidden;
    box-shadow: 0 6px 16px rgba(0,0,0,0.25);
  }
  .card--front { top: 73px; background: var(--matrix-deep); }
  .card--back { top: 533px; background: var(--card-black); }

  .front-photo {
    position: absolute; inset: 0;
    background: linear-gradient(100deg, var(--photo-light) 0%, var(--matrix-mid) 40%, var(--matrix-deep) 100%);
  }
  .brand-title {
    position: absolute;
    left: 311px; top: 176px;
    font-family: "Cinzel", serif;
    font-weight: 400;
    font-size: 40px;
    color: var(--text-white);
    letter-spacing: 0.5px;
    white-space: nowrap;
  }

  .identity {
    position: absolute;
    right: 354px; top: 162px;
    text-align: right;
  }
  .identity__name {
    font-family: "Bebas Neue", sans-serif;
    font-size: 42px;
    line-height: 1;
    color: var(--accent-green);
    letter-spacing: 0.5px;
    white-space: nowrap;
  }
  .identity__role {
    font-family: "Open Sans", sans-serif;
    font-size: 15px;
    color: var(--text-white);
    margin-top: 4px;
  }
  .divider {
    position: absolute;
    left: 332px; top: 155px;
    width: 1px; height: 90px;
    background: linear-gradient(180deg, transparent, var(--divider) 30%, var(--divider) 70%, transparent);
  }
  .contacts {
    position: absolute;
    left: 354px; top: 162px;
    list-style: none;
    font-family: "Open Sans", sans-serif;
    font-size: 15px;
    color: var(--text-white);
  }
  .contacts li { display: flex; align-items: center; height: 23px; white-space: nowrap; }
  .contacts svg { width: 14px; height: 14px; margin-right: 7px; fill: var(--accent-green); }
  .address {
    position: absolute;
    left: 135px; top: 346px;
    display: flex; align-items: center;
    font-family: "Open Sans", sans-serif;
    font-size: 16px;
    letter-spacing: 0.6px;
    color: var(--text-white);
    white-space: nowrap;
  }
  .address svg { width: 14px; height: 18px; margin-right: 6px; fill: var(--accent-green); }
</style>
</head>
<body>
  <section class="card card--front">
    <div class="front-photo" role="img" aria-label="Headshot of the consultant in suit and tie with a green falling-code effect"></div>
    <h1 class="brand-title">Kestrel Works</h1>
  </section>

  <section class="card card--back">
    <div class="identity">
      <div class="identity__name">Omar Delacroix</div>
      <div class="identity__role">Consultant</div>
    </div>
    <div class="divider"></div>
    <ul class="contacts">
      <li><svg viewBox="0 0 14 14"><path d="M4 0h6a1 1 0 0 1 1 1v12a1 1 0 0 1-1 1H4a1 1 0 0 1-1-1V1a1 1 0 0 1 1-1zm0 2v9h6V2z"/></svg>+ 000 000 0000</li>
      <li><svg viewBox="0 0 14 14"><path d="M1 4c2-2 10-2 12 0v2h-3V4.5c-2-.6-4-.6-6 0V6H1zm3 3h6l2 3v3H2v-3z"/></svg>+ 000 000 0000</li>
      <li><svg viewBox="0 0 14 14"><path d="M0 3h14v1L7 8 0 4zm0 2.3l7 4 7-4V12H0z"/></svg>info@omardelacroix.com</li>
    </ul>
    <div class="address">
      <svg viewBox="0 0 14 18"><path d="M7 0a7 7 0 0 1 7 7c0 5-7 11-7 11S0 12 0 7a7 7 0 0 1 7-7zm0 4a3 3 0 1 0 0 6 3 3 0 0 0 0-6z"/></svg>
      2415 Harbor View Rd 8 St, Fairmont, MD 21090
    </div>
  </section>
</body>
</html>
```